Corndell website

Provide a website for a business that is an online farmstand for mostly organic farm products produced on our 9 farms and packaged at our mill. We will be targeting an urban and suburban audience that will be able know the farms where their food is grown and "pick" their food online. We want the site to feel to feel fresh and urbane. Winning logo attached.

The website will feature:

A section with descriptions, pictures and Google maps for the farms as well as the produce produced on each farm. We will want to establish a provenance to the mostly organic food we produce and sell - and visit the farms if they want. We want our customers to know where their food comes from without having to live on a farm. We will market products of local farmers in addition to our own. We'll need room for about 50 farm descriptions and about 5 product descriptions per farm.

A master growing schedule -- there should be room for about 5 products per farm.

An online store (maybe linked to the farm and product) descriptions

An about us section -- where we can tell our family's story and about the history of the mill where we package food and provide fulfillment

A section for links to other farming and food information

A section for legal notices
Updates

Project Deadline Extended
Reason: Holiday weekend for many in USA

Target Market(s)

Educated, urban market who wants quality food at fair prices.

Industry/Entity Type

Farm

```html
<!DOCTYPE html>
<html lang="en">
<head>
<meta charset="utf-8">
<title>Corndell — Online Farmstand</title>
<link rel="stylesheet" href="https://fonts.googleapis.com/css2?family=Josefin+Sans:wght@600;700&family=Dancing+Script:wght@600&family=PT+Serif:ital@0;1&family=Source+Sans+3:wght@400;600;700&family=Kaushan+Script&display=swap">
<style>
:root{
  --plum:#3a2228;
  --green:#6e8f17;
  --text:#555;
  --muted:#888;
  --line:#3a2228;
  --rule:#ccc;
  --bg:#fff;
}
*{box-sizing:border-box;margin:0;padding:0}
html,body{width:740px;height:1200px;overflow:hidden;background:var(--bg)}
body{font-family:"Source Sans 3",sans-serif;color:var(--text)}
.page{position:relative;width:740px;height:1200px;overflow:hidden}
.abs{position:absolute}
a{color:inherit;text-decoration:none}

/* header */
.cart{left:92px;top:9px;font-size:10px;display:flex;align-items:center;gap:4px}
.cart-label{font-family:"Kaushan Script",cursive;color:#8a3b1a;font-size:11px}
.social-mini{left:92px;top:57px;display:flex;gap:4px}
.social-mini span{width:9px;height:9px;background:#777;display:block}
.brand{left:0;width:740px;top:12px;text-align:center}
.brand-dot{width:14px;height:14px;border-radius:50%;background:var(--plum);margin:0 auto 20px}
.brand-name{font-family:"Josefin Sans",sans-serif;font-weight:700;font-size:18px;color:var(--plum);letter-spacing:2px}
.call{right:92px;top:56px;font-size:10px;color:#444}

.nav{left:92px;width:556px;top:80px;height:25px;border-top:2px solid var(--line);border-bottom:3px solid var(--line);display:flex;justify-content:space-between;align-items:center;padding:2px 14px 0}
.nav a{font-family:"Josefin Sans",sans-serif;font-weight:700;font-size:10px;color:var(--plum);text-transform:uppercase}
.nav a.current{color:var(--green)}

/* hero */
.small{font-size:7px;line-height:9px;color:var(--muted)}
.kicker{font-family:"Josefin Sans",sans-serif;font-weight:700;color:var(--green);text-transform:uppercase;line-height:1;white-space:nowrap}
.script{font-family:"Dancing Script",cursive;color:var(--plum);line-height:1;white-space:nowrap}
.hero-left{left:96px;width:160px}
.dotted{border-top:1px dotted #555;height:0}
.dots{left:96px;top:318px;display:flex;gap:2px}
.dots span{width:9px;height:9px;border-radius:50%;background:var(--green)}
.hero-pie{left:270px;top:132px;width:194px;height:206px;border-radius:50%;background:conic-gradient(#c9a06a 0 25%,#d2a04a 25% 45%,#8fb34a 45% 60%,#e3c94f 60% 75%,#d79a8a 75% 100%)}
.hero-wheat{left:434px;top:256px;width:68px;height:68px;border-radius:50%;background:radial-gradient(circle at 50% 30%,#5c7fb0,#d9a032 70%);border:2px solid #fff}
.hero-right{left:480px;width:168px;text-align:center}
.hero-title{font-family:"Josefin Sans",sans-serif;font-weight:700;font-size:17px;line-height:18px;color:var(--plum);white-space:nowrap;letter-spacing:.2px}
.serif{font-family:"PT Serif",serif}

/* welcome */
.welcome{left:92px;width:556px;top:374px;display:flex;align-items:center;gap:10px}
.welcome::before,.welcome::after{content:"";flex:1;border-top:1px solid var(--plum)}
.welcome h1{font-family:"Josefin Sans",sans-serif;font-weight:700;font-size:18px;color:var(--plum);letter-spacing:.3px}
.photo{top:426px;width:96px;height:105px}
.intro{left:240px;width:260px;top:417px;text-align:center;font-family:"PT Serif",serif;font-size:9px;line-height:12px;color:#777}
.intro-head{left:150px;width:440px;top:468px;text-align:center;font-size:13px}
.col-note{top:505px;width:128px;text-align:center;font-size:7px;line-height:9.5px;color:#333}
.mark{left:362px;top:507px;width:12px;height:12px;border-radius:50%;border:1.5px solid var(--plum)}

/* products */
.products{left:90px;width:558px;display:grid;grid-template-columns:repeat(6,93px)}
.product{height:178px;text-align:center;padding-top:6px;position:relative}
.product.active{outline:1px solid #e2e2e2;box-shadow:0 0 4px rgba(0,0,0,.08)}
.thumb{width:66px;height:66px;margin:0 auto 14px;border-radius:50%}
.p-name{font-size:8px;font-weight:600;color:#111;margin-bottom:7px}
.p-desc{font-size:7px;line-height:9px;color:var(--muted)}
.p-price{font-size:9px;color:#333;margin:3px 0 9px}
.add{display:inline-flex;align-items:center;gap:3px;font-size:6.5px;font-weight:700;color:var(--plum);border:1px solid #ddd;box-shadow:0 1px 1px rgba(0,0,0,.1);padding:2px 5px}
.product.active .add{background:var(--plum);color:#fff;border-color:var(--plum)}

/* banner */
.banner{left:92px;width:556px;top:1003px;height:37px;border-top:1px solid var(--plum);border-bottom:2px solid var(--plum);display:flex;align-items:center;gap:10px;padding-left:28px}
.banner-icon{width:25px;height:25px;border-radius:50%;background:#e6e6e6;display:flex;align-items:center;justify-content:center}
.banner-text{font-family:"Kaushan Script",cursive;color:#a0471f;font-size:10px}
.banner-text span{font-family:"PT Serif",serif;color:#777;font-size:10px}

/* footer */
.f-col{top:1058px}
.f-col h3{font-family:"PT Serif",serif;font-weight:400;font-size:11px;color:#222;margin-bottom:8px}
.f-text{font-size:7px;line-height:9px;color:#333}
.field{width:118px;height:13px;border:1px solid #bbb;border-radius:2px;font-size:7px;padding:2px 4px;color:#555;margin:7px 0 4px}
.btn{display:inline-block;background:var(--plum);color:#fff;font-size:7px;padding:1px 6px;border-radius:2px}
.follow{display:flex;align-items:center;gap:6px;font-size:9px;color:#444;margin-bottom:6px}
.follow i{width:12px;height:12px;background:#555;display:block}
.bottom{left:92px;width:556px;top:1153px;border-top:1px solid var(--rule);padding-top:10px;display:flex;justify-content:space-between;font-size:7px;color:#333}
.bottom nav{display:flex;gap:15px}
.bottom nav a.current{color:var(--green)}
</style>
</head>
<body>
<div class="page">

  <header>
    <div class="abs cart">
      <svg width="10" height="9" viewBox="0 0 10 9"><path d="M1 3h8l-1 5H2z" fill="none" stroke="#444"/><path d="M3 3l2-2 2 2" fill="none" stroke="#444"/></svg>
      <span class="cart-label">Shopping Cart</span><span>(00 items)</span>
    </div>
    <div class="abs social-mini"><span></span><span></span><span></span></div>
    <div class="abs brand"><div class="brand-dot"></div><div class="brand-name">CORNDELL</div></div>
    <div class="abs call">Call Us: 000-000-0000</div>
    <nav class="abs nav">
      <a class="current" href="#">Home</a><a href="#">About</a><a href="#">Store</a><a href="#">Farms</a><a href="#">Food</a><a href="#">Master Growing Schedule</a><a href="#">Leagal</a><a href="#">Contact</a>
    </nav>
  </header>

  <section class="hero">
    <div class="abs hero-left small" style="top:153px">Sed feugiat mollis neque. Suspendisse potenti. Sed dui, consequat vel ultrices quis, faucibus</div>
    <div class="abs hero-left script" style="top:170px;font-size:29px">integer eget</div>
    <div class="abs hero-left kicker" style="top:203px;font-size:6.5px">Etiam non felis mi. Quisque feugiat.</div>
    <div class="abs hero-left dotted" style="top:240px;width:96px"></div>
    <div class="abs hero-left small" style="top:265px;color:#666;width:165px">Sed feugiat mollis neque. Suspendisse potenti. Seddui, consequat vel ultrices quis, faucibus iaculis nisi. Pellentesque sit amet eleifend augue.</div>
    <div class="abs hero-left kicker" style="top:296px;font-size:9px">Pellentesque</div>
    <div class="abs dots"><span></span><span></span><span></span></div>

    <svg class="abs" style="left:228px;top:133px" width="66" height="26" viewBox="0 0 66 26"><path d="M2 10 Q30 -6 60 20" fill="none" stroke="#555"/><path d="M54 19l6 2-1-6" fill="none" stroke="#555"/></svg>
    <div class="abs hero-pie" role="img" aria-label="Pie arrangement of breads, fruit, vegetables, meat, eggs and dairy"></div>
    <div class="abs hero-wheat" role="img" aria-label="Wheat field under blue sky"></div>

    <div class="abs hero-right serif" style="top:144px;font-size:9px;line-height:11px;color:#222;white-space:nowrap">Luctus et ultrices posuere cubilia</div>
    <div class="abs hero-right hero-title" style="top:155px">ETIAM ET TELLUS</div>
    <div class="abs hero-right kicker" style="top:175px;font-size:8.5px">Nam quis • Fermentum</div>
    <div class="abs hero-right serif" style="top:188px;font-size:7px;line-height:9px;color:#444">Sed feugiat mollis neque. Suspendisse potenti.<br>Sed libero dui, consequat vel ultrices quis,</div>
    <div class="abs dotted" style="left:500px;top:220px;width:126px"></div>
    <div class="abs hero-right kicker" style="top:238px;font-size:8.5px">Pellentesque</div>
    <div class="abs hero-right script" style="top:245px;font-size:25px">pretium</div>
    <div class="abs hero-right kicker" style="top:270px;font-size:6.5px">Vulputate pellentesque</div>
    <div class="abs small" style="left:508px;top:297px;width:130px;color:#444">Cras eget sollicitudin lectus. In vel turpis lacus, vitae fringilla urna. Etiam et tellus vel turpis cursus egestas ut vel risus.</div>
  </section>

  <section>
    <div class="abs welcome"><h1>WELCOME TO CORNDELL</h1></div>
    <div class="abs photo" style="left:98px;background:linear-gradient(#7b93b0,#a9b6c1 35%,#d7a23c 50%,#a46d1c)" role="img" aria-label="Ripe wheat field under cloudy sky"></div>
    <div class="abs photo" style="left:546px;background:linear-gradient(#4d524a,#6f7561 45%,#5b6b3e)" role="img" aria-label="Farm workers in straw hats tending seedlings"></div>
    <p class="abs intro">Vestibulum ante ipsum primis in faucibus orci luctus et ultrices posuere cubilia Curae; Vestibulum ac nibh eget enim sollicitudin tincidunt et ac lorem. Cras eget sollicitudin lectus.</p>
    <h2 class="abs intro-head kicker">Etiam non felis mi. Quisque feugiat</h2>
    <p class="abs col-note" style="left:217px">Sed feugiat mollis neque. Suspendisse potenti. Seddui, consequat vel ultrices quis, faucibus iaculis nisi.</p>
    <div class="abs mark"></div>
    <p class="abs col-note" style="left:394px">Etiam non felis mi. Quisque feugiat, lectus non feugiat consectetur, purus ipsum lobortis nisl, a sollicitudin</p>
  </section>

  <section class="abs products" style="top:584px;row-gap:30px">
    <div class="product"><div class="thumb" role="img" aria-label="Rice grains" style="background:radial-gradient(#fbf6ea,#e9dfc6 60%,#fff 72%)"></div><div class="p-name">Product Name</div><div class="p-desc">Sed feugiat mollis neque.<br>Suspendisse potenti.</div><div class="p-price">$ 00.00</div><span class="add">ADD <svg width="7" height="6" viewBox="0 0 7 6"><path d="M0 1h7l-1 5H1z" fill="currentColor"/></svg></span></div>
    <div class="product"><div class="thumb" role="img" aria-label="Brown eggs" style="background:radial-gradient(#e8a16e,#c87841 55%,#fff 72%)"></div><div class="p-name">Product Name</div><div class="p-desc">Sed feugiat mollis neque.<br>Suspendisse potenti.</div><div class="p-price">$ 00.00</div><span class="add">ADD <svg width="7" height="6" viewBox="0 0 7 6"><path d="M0 1h7l-1 5H1z" fill="currentColor"/></svg></span></div>
    <div class="product"><div class="thumb" role="img" aria-label="Glass of milk" style="background:radial-gradient(#f4f4f2,#dcdcd8 55%,#fff 72%)"></div><div class="p-name">Product Name</div><div class="p-desc">Sed feugiat mollis neque.<br>Suspendisse potenti.</div><div class="p-price">$ 00.00</div><span class="add">ADD <svg width="7" height="6" viewBox="0 0 7 6"><path d="M0 1h7l-1 5H1z" fill="currentColor"/></svg></span></div>
    <div class="product active"><div class="thumb" role="img" aria-label="Raw red meat with herbs" style="background:radial-gradient(#d5545a,#b23a40 55%,#fff 72%)"></div><div class="p-name">Product Name</div><div class="p-desc">Sed feugiat mollis neque.<br>Suspendisse potenti.</div><div class="p-price">$ 00.00</div><span class="add">ADD <svg width="7" height="6" viewBox="0 0 7 6"><path d="M0 1h7l-1 5H1z" fill="currentColor"/></svg></span></div>
    <div class="product"><div class="thumb" role="img" aria-label="Wheat ears" style="background:radial-gradient(#e6bf72,#cf9a45 50%,#fff 72%)"></div><div class="p-name">Product Name</div><div class="p-desc">Sed feugiat mollis neque.<br>Suspendisse potenti.</div><div class="p-price">$ 00.00</div><span class="add">ADD <svg width="7" height="6" viewBox="0 0 7 6"><path d="M0 1h7l-1 5H1z" fill="currentColor"/></svg></span></div>
    <div class="product"><div class="thumb" role="img" aria-label="Fresh fish" style="background:radial-gradient(#8d8f8c,#6b6d6a 50%,#fff 72%)"></div><div class="p-name">Product Name</div><div class="p-desc">Sed feugiat mollis neque.<br>Suspendisse potenti.</div><div class="p-price">$ 00.00</div><span class="add">ADD <svg width="7" height="6" viewBox="0 0 7 6"><path d="M0 1h7l-1 5H1z" fill="currentColor"/></svg></span></div>

    <div class="product"><div class="thumb" role="img" aria-label="Mixed grains and seeds" style="background:radial-gradient(#b88a4a,#8a5a2c 55%,#fff 72%)"></div><div class="p-name">Product Name</div><div class="p-desc">Sed feugiat mollis neque.<br>Suspendisse potenti.</div><div class="p-price">$ 00.00</div><span class="add">ADD <svg width="7" height="6" viewBox="0 0 7 6"><path d="M0 1h7l-1 5H1z" fill="currentColor"/></svg></span></div>
    <div class="product"><div class="thumb" role="img" aria-label="Honey jar and honeycomb" style="background:radial-gradient(#f4b63a,#e08d14 55%,#fff 72%)"></div><div class="p-name">Product Name</div><div class="p-desc">Sed feugiat mollis neque.<br>Suspendisse potenti.</div><div class="p-price">$ 00.00</div><span class="add">ADD <svg width="7" height="6" viewBox="0 0 7 6"><path d="M0 1h7l-1 5H1z" fill="currentColor"/></svg></span></div>
    <div class="product"><div class="thumb" role="img" aria-label="Assorted vegetables" style="background:radial-gradient(#7aa33a,#c2482e 45%,#fff 70%)"></div><div class="p-name">Product Name</div><div class="p-desc">Sed feugiat mollis neque.<br>Suspendisse potenti.</div><div class="p-price">$ 00.00</div><span class="add">ADD <svg width="7" height="6" viewBox="0 0 7 6"><path d="M0 1h7l-1 5H1z" fill="currentColor"/></svg></span></div>
    <div class="product"><div class="thumb" role="img" aria-label="Bowl of mixed nuts" style="background:radial-gradient(#a8663a,#7a4624 50%,#fff 72%)"></div><div class="p-name">Product Name</div><div class="p-desc">Sed feugiat mollis neque.<br>Suspendisse potenti.</div><div class="p-price">$ 00.00</div><span class="add">ADD <svg width="7" height="6" viewBox="0 0 7 6"><path d="M0 1h7l-1 5H1z" fill="currentColor"/></svg></span></div>
    <div class="product"><div class="thumb" role="img" aria-label="Lemons" style="background:radial-gradient(#ffe34a,#f2c20d 55%,#fff 72%)"></div><div class="p-name">Product Name</div><div class="p-desc">Sed feugiat mollis neque.<br>Suspendisse potenti.</div><div class="p-price">$ 00.00</div><span class="add">ADD <svg width="7" height="6" viewBox="0 0 7 6"><path d="M0 1h7l-1 5H1z" fill="currentColor"/></svg></span></div>
    <div class="product"><div class="thumb" role="img" aria-label="Tomatoes" style="background:radial-gradient(#e2402a,#b9230f 55%,#fff 72%)"></div><div class="p-name">Product Name</div><div class="p-desc">Sed feugiat mollis neque.<br>Suspendisse potenti.</div><div class="p-price">$ 00.00</div><span class="add">ADD <svg width="7" height="6" viewBox="0 0 7 6"><path d="M0 1h7l-1 5H1z" fill="currentColor"/></svg></span></div>
  </section>

  <aside class="abs banner">
    <div class="banner-icon"><svg width="13" height="12" viewBox="0 0 13 12"><path d="M1 1h2l2 7h6l1-5H4" fill="none" stroke="#444" stroke-width="1.2"/><circle cx="6" cy="10.5" r="1" fill="#444"/><circle cx="10" cy="10.5" r="1" fill="#444"/></svg></div>
    <p class="banner-text">Etiam eros velit, rutrum in fringilla id, fermentum sit amet nulla : <span>faucibus orci luctus et ultrices</span></p>
  </aside>

  <footer>
    <div class="abs f-col" style="left:97px;width:130px">
      <h3>Newsletter Signup</h3>
      <p class="f-text">Sign up with your email to recieve our free newsletter monthly.</p>
      <div class="field">enter your email id</div>
      <span class="btn">Submit</span>
    </div>
    <div class="abs f-col" style="left:254px">
      <h3>Follow Us</h3>
      <div class="follow"><i></i>Grangebook</div>
      <div class="follow"><i></i>Chirper</div>
      <div class="follow"><i></i>ClipCast</div>
    </div>
    <div class="abs f-col" style="left:360px;width:125px">
      <h3>Our Store</h3>
      <p class="f-text" style="margin-bottom:5px">Sed feugiat mollis neque. Suspendisse potenti. Seddui, consequat vel ultrices quis, faucibus iaculis nisi.</p>
      <span class="btn">Details</span>
    </div>
    <div class="abs f-col" style="left:510px;width:135px">
      <h3>Contact Us</h3>
      <p class="f-text" style="margin-bottom:9px">Sed feugiat mollis neque. Suspendisse potenti. Seddui, consequat vel</p>
      <p class="f-text"><b>Email:</b> hello@corndellfarms.net<br><b>Phone:</b> 000-000-0000</p>
    </div>
    <div class="abs bottom">
      <nav><a class="current" href="#">Home</a><a href="#">About</a><a href="#">Store</a><a href="#">Farms</a><a href="#">Food</a><a href="#">Master growing schedule</a><a href="#">Leagal</a><a href="#">Contact</a></nav>
      <span>© Copyright 2013. All Rights Reserved</span>
    </div>
  </footer>

</div>
</body>
</html>
```